Business Card for Start Up Real Estate Company

We need a business card designed for a new real estate company called Belvanta. We plan on improving the experience of real estate transactions for both consumers and agents by using current and evolving technology. We would like to see designs that use our existing logo (attached). Please use a primarily white or light colored background. The final design should communicate technology, sophistication and customer service. Thank you...

Industry/Entity Type

Real Estate

Requirements
Must have
• Primarily white or light colored background
Nice to have
• Isolated A from our logo used as part of the design
Should not have
• Pictures, especially of houses

```html
<!DOCTYPE html>
<html lang="en">
<head>
<meta charset="utf-8">
<title>Belvanta – Business Card</title>
<link rel="stylesheet" href="https://fonts.googleapis.com/css2?family=Open+Sans:wght@600&family=Varela+Round&display=swap">
<style>
  :root {
    --card-bg: #ffffff;
    --brand-blue: #1f4f8f;
    --text-blue: #2b5c98;
    --tagline-blue: #b7c9dd;
    --deco-blue: rgba(205, 218, 232, 0.95);
    --deco-blue-soft: rgba(205, 218, 232, 0.6);
    --deco-pink: rgba(247, 204, 212, 0.75);
    --deco-pink-clear: rgba(247, 204, 212, 0);
  }
  html, body {
    margin: 0;
    padding: 0;
    width: 1200px;
    height: 702px;
    overflow: hidden;
    background: var(--card-bg);
  }
  .card {
    position: relative;
    width: 1200px;
    height: 702px;
    background: var(--card-bg);
    overflow: hidden;
    font-family: "Open Sans", Arial, sans-serif;
  }
  .brand-backdrop {
    position: absolute;
    left: 0;
    top: 0;
    width: 820px;
    height: 702px;
    background: linear-gradient(155deg,
      var(--deco-blue) 0%,
      var(--deco-blue-soft) 38%,
      var(--deco-pink) 62%,
      var(--deco-pink-clear) 100%);
  }
  .tagline {
    position: absolute;
    right: 147px;
    top: 36px;
    margin: 0;
    font-family: "Varela Round", "Open Sans", sans-serif;
    font-size: 65px;
    line-height: 1;
    color: var(--tagline-blue);
    white-space: nowrap;
  }
  .brand-name {
    position: absolute;
    right: 61px;
    top: 107px;
    margin: 0;
    font-family: "Open Sans", Arial, sans-serif;
    font-weight: 600;
    font-size: 84px;
    line-height: 1;
    color: var(--brand-blue);
    letter-spacing: 1px;
    white-space: nowrap;
  }
  .contact {
    position: absolute;
    right: 65px;
    top: 280px;
    margin: 0;
    text-align: right;
    font-style: normal;
    font-weight: 600;
    font-size: 40px;
    line-height: 44px;
    letter-spacing: 1.3px;
    color: var(--text-blue);
    white-space: nowrap;
  }
  .contact p { margin: 0; }
  .contact .group { margin-bottom: 53px; }
  .contact .group:last-child { margin-bottom: 0; }
</style>
</head>
<body>
  <main class="card">
    <div class="brand-backdrop" role="img" aria-label="Large faint brand letter A with a sweeping red curve, in pale blue and pale pink"></div>
    <p class="tagline">real estate company</p>
    <h1 class="brand-name">Belvanta</h1>
    <address class="contact">
      <div class="group">
        <p class="person-name">Jonas Feldberg</p>
      </div>
      <div class="group">
        <p class="phone">0176-382 519 07</p>
        <p class="email">Jonas.Feldberg@belvanta.com</p>
      </div>
      <div class="group">
        <p class="street">Lindenweg 14</p>
        <p class="city">20457 Hafenstadt</p>
      </div>
    </address>
  </main>
</body>
</html>
```